W.I.Q 'Wadi Ibn Qutub' for General Transportation

this company is a Iraqi based company.
It provides a number of logistics activities such as;
Overland Transportation
High and heavy logistics
Customs clearance
warehousing
Automotive logistics
The company has been registered since 2009.
If you have any other questions please feel free to ask.
Target Market(s)
Automotive
White goods
All Trading sectors
Industry/Entity Type
Automotive

```html
<!DOCTYPE html>
<html lang="en">
<head>
<meta charset="utf-8">
<title>Wadi Ibn Qutub Transportation</title>
<link href="https://fonts.googleapis.com/css2?family=Open+Sans:wght@300;400;600;700&display=swap" rel="stylesheet">
<style>
:root{
  --navy:#1d3a6c;
  --navy-dark:#163058;
  --text:#8b8b8b;
  --band:#f2f2f2;
  --panel:#f6f6f6;
  --white:#ffffff;
  --badge:#cfd3d8;
}
*{margin:0;padding:0;box-sizing:border-box}
html,body{width:910px;height:1200px;overflow:hidden;background:var(--white);font-family:'Open Sans',Arial,sans-serif}
.page{position:relative;width:910px;height:1200px}
.abs{position:absolute}

.logo{left:133px;top:20px;width:100px;text-align:center;color:var(--navy)}
.logo-mark{font-size:30px;font-weight:700;line-height:34px;letter-spacing:1px}
.logo-name{font-size:6.5px;line-height:8px;color:var(--navy)}
.logo-sub{font-size:6.5px;line-height:8px;color:#7a8aa8}
.logo-url{font-size:5px;line-height:7px;color:var(--navy)}

.nav{top:38px;left:301px;display:flex;gap:24px;font-size:12px;color:var(--navy)}
.lang{left:726px;top:36px;width:86px;height:23px;border:1px solid #cfcfcf;background:#f4f4f4;display:flex;align-items:center;padding-left:7px;gap:4px;font-size:9px;color:#9a9a9a}
.lang .flag{width:19px;height:12px;background:#2a4a8a;border:1px solid #c33}
.lang .caret{margin-left:auto;margin-right:8px;font-size:8px;color:#666}

.hero{left:0;top:88px;width:910px;height:315px;background:linear-gradient(100deg,#1a2640 0%,#2b4f8a 45%,#1c2f55 70%,#4a5a70 100%)}
.dots{left:430px;top:366px;display:flex;gap:4px}
.dots span{width:10px;height:10px;border-radius:50%;background:var(--white)}
.dots span:first-child{background:var(--navy)}

.services{left:0;top:403px;width:910px;height:271px;background:var(--band)}
.section-title{font-size:11px;font-weight:700;color:var(--navy)}
.services .section-title{left:0;width:910px;text-align:center;top:20px}
.arrow{top:24px}
.cards{left:98px;top:52px;display:flex;gap:15px}
.card{width:167px}
.card .photo{width:167px;height:106px}
.card h3{font-size:11.5px;font-weight:400;color:var(--navy);margin-top:11px;margin-left:-1px}
.card p{font-size:8.6px;line-height:13.6px;color:var(--text);margin-top:10px;font-weight:300}

.welcome{left:98px;top:716px;width:470px}
.welcome .photo{width:469px;height:142px;margin-top:12px;background:linear-gradient(90deg,#3a3a40 0%,#9a8f80 40%,#c8c4bb 70%,#8a8a8a 100%)}
.welcome p{font-size:8.6px;line-height:18.2px;color:var(--text);margin-top:9px;font-weight:300}

.news{left:584px;top:701px;width:228px;height:322px;background:var(--panel);padding:16px 15px}
.news-head{display:flex;justify-content:space-between;align-items:center}
.news-item{display:flex;gap:12px;margin-top:15px}
.news-item:first-of-type{margin-top:19px}
.news-item .thumb{width:77px;height:52px;flex:none}
.news-item h4{font-size:9px;line-height:13.5px;font-weight:700;color:#777}
.news-item p{font-size:8.6px;line-height:13.5px;color:var(--text);font-weight:300}

.press{left:106px;top:1066px;display:flex;align-items:center;gap:26px}
.press span{height:22px;background:var(--badge);border-radius:3px}

.footer{left:0;top:1125px;width:910px;height:75px;background:var(--navy)}
.footer-nav{top:15px;left:0;width:910px;display:flex;justify-content:center;gap:18px;font-size:11.5px;color:var(--white)}
.footer-nav .sep{opacity:.9}
.copy{top:44px;left:0;width:910px;text-align:center;font-size:11.5px;color:var(--white)}
</style>
</head>
<body>
<div class="page">

  <header>
    <div class="abs logo">
      <div class="logo-mark">W.I.Q</div>
      <div class="logo-name">Wadi Ibn Qutub</div>
      <div class="logo-sub">Transportation</div>
      <div class="logo-url">www.wiqtransport.com</div>
    </div>
    <nav class="abs nav">
      <span>Home</span><span>About Us</span><span>Services</span><span>Logistics</span><span>Partners</span><span>Contact Us</span>
    </nav>
    <div class="abs lang"><span class="flag"></span><span>English</span><span class="caret">▼</span></div>
  </header>

  <div class="abs hero" role="img" aria-label="Blue trucks parked at dusk under a dark blue sky"></div>
  <div class="abs dots"><span></span><span></span><span></span><span></span></div>

  <section class="abs services">
    <h2 class="abs section-title">SERVICES</h2>
    <svg class="abs arrow" style="left:98px" width="10" height="14" viewBox="0 0 10 14"><path d="M8 1L2 7l6 6" fill="none" stroke="#111" stroke-width="2.2"/></svg>
    <svg class="abs arrow" style="left:799px" width="10" height="14" viewBox="0 0 10 14"><path d="M2 1l6 6-6 6" fill="none" stroke="#111" stroke-width="2.2"/></svg>
    <div class="abs cards">
      <div class="card">
        <div class="photo" role="img" aria-label="Container ship at sea" style="background:linear-gradient(180deg,#8fb4d8 0%,#a8c6e0 50%,#4b7fa6 70%,#2f6a90 100%)"></div>
        <h3>Overland Transportation</h3>
        <p>Sed ut perspiciatis unde omnis iste natus error sit voluptatem accusantium doloremque laudantium, totam rem aperiam, eaque ipsa quae ab</p>
      </div>
      <div class="card">
        <div class="photo" role="img" aria-label="Container port cranes at dusk" style="background:linear-gradient(180deg,#2d5b9a 0%,#6a86a8 45%,#c79a5e 75%,#8a6040 100%)"></div>
        <h3>High and heavy logistics</h3>
        <p>Sed ut perspiciatis unde omnis iste natus error sit voluptatem accusantium doloremque laudantium, totam rem aperiam, eaque ipsa quae ab</p>
      </div>
      <div class="card">
        <div class="photo" role="img" aria-label="Warehouse stacked with cardboard boxes" style="background:linear-gradient(180deg,#6b5f55 0%,#b39878 50%,#d6c6b2 100%)"></div>
        <h3>Customs Clearance</h3>
        <p>Sed ut perspiciatis unde omnis iste natus error sit voluptatem accusantium doloremque laudantium, totam rem aperiam, eaque ipsa quae ab</p>
      </div>
      <div class="card">
        <div class="photo" role="img" aria-label="Cargo being loaded onto an aircraft" style="background:linear-gradient(90deg,#c9c9c9 0%,#e2ddd6 50%,#9a8a78 100%)"></div>
        <h3>Warehousing</h3>
        <p>Sed ut perspiciatis unde omnis iste natus error sit voluptatem accusantium doloremque laudantium, totam rem aperiam, eaque ipsa quae ab</p>
      </div>
    </div>
  </section>

  <section class="abs welcome">
    <h2 class="section-title">WELCOME TO WADI IBN QUTUB</h2>
    <div class="photo" role="img" aria-label="Forklifts in a warehouse with tall shelving"></div>
    <p>Sed ut perspiciatis unde omnis iste natus error sit voluptatem accusantium doloremque laudantium, totam rem aperiam, eaque ipsa quae ab illo inventore veritatis et quasi architecto beatae vitae dicta sunt explicabo. Nemo enim ipsam voluptatem quia voluptas sit aspernatur aut odit aut fugit, sed quia consequuntur magni dolores eos qui ratione voluptatem sequi nesciunt. Neque porro quisquam est, qui dolorem ipsum quia dolor sit amet, consectetur, adipisci velit, sed quia non numquam eius modi tempora incidunt ut labore et dolore magnam aliquam quaerat voluptatem. Ut enim ad minima veniam, quis nostrum exercitationem</p>
  </section>

  <aside class="abs news">
    <div class="news-head">
      <h2 class="section-title">LATEST NEWS</h2>
      <svg width="22" height="14" viewBox="0 0 22 14"><path d="M8 1L2 7l6 6M14 1l6 6-6 6" fill="none" stroke="#111" stroke-width="2"/></svg>
    </div>
    <div class="news-item">
      <div class="thumb" role="img" aria-label="Port crane loading a container" style="background:linear-gradient(180deg,#c8a050 0%,#b07a30 50%,#8a8a8a 100%)"></div>
      <div><h4>Sed ut perspiciatis unde omnis iste natus</h4><p>Error sit voluptatem accusantium doloremque laudantium, totam</p></div>
    </div>
    <div class="news-item">
      <div class="thumb" role="img" aria-label="Container ship at sea" style="background:linear-gradient(180deg,#9ab9d8 0%,#4f7fa8 60%,#2a5a86 100%)"></div>
      <div><h4>Sed ut perspiciatis unde omnis iste natus</h4><p>Error sit voluptatem accusantium doloremque laudantium, totam</p></div>
    </div>
    <div class="news-item">
      <div class="thumb" role="img" aria-label="Hand touching a digital world map screen" style="background:linear-gradient(135deg,#0e2a4a 0%,#2f6aa0 60%,#6aa0c8 100%)"></div>
      <div><h4>Sed ut perspiciatis unde omnis iste natus</h4><p>Error sit voluptatem accusantium doloremque laudantium, totam</p></div>
    </div>
  </aside>

  <div class="abs press" aria-label="Press mentions">
    <span style="width:96px"></span>
    <span style="width:60px"></span>
    <span style="width:38px;border-radius:50%;height:26px"></span>
    <span style="width:120px"></span>
    <span style="width:103px"></span>
    <span style="width:142px"></span>
  </div>

  <footer class="abs footer">
    <nav class="abs footer-nav">
      <span>Home</span><span class="sep">|</span><span>About Us</span><span class="sep">|</span><span>Services</span><span class="sep">|</span><span>Logistics</span><span class="sep">|</span><span>Partners</span><span class="sep">|</span><span>Contact Us</span>
    </nav>
    <div class="abs copy">© Copyright 2014 ,Company Name All Right&nbsp; Reserved</div>
  </footer>

</div>
</body>
</html>
```